Label for Dog Nourishing CBD Balm

Dear Designers,

We are looking for a packaging expert to design our new Hydrating Balm for dogs which contain a relaxing hemp extract (CBD). The product is intended to be massaged on the dog’s paws to make them softer and promote the animal’s well-being :)

Our company is already selling various relaxing cat & dog products, and we would like this new design to reflect the same "style & feeling" as our current products (see attached ZIP file).

Technical aspects:
- The packaging is a 40ml aluminium jar (58mm x 23mm).
- We are looking to design 2 separate labels (one for the front, one for the back)
- The label dimensions should be : 50mm x 50mm
- Please follow technical guidelines from printer (see ZIP file).

Design aspects:
- The design should be compatible with our brand identity (i.e. fluffly, pure, relaxing, positive, clean & natural).
- People should understand what the product "is" and what the product "does" simply from looking at the design.
- The actual balm is white/yellow in color.
- Soft/rounded shapes are preferred.
- Please use our brand's colors (see typo & colors in ZIP file)
- Please use our brand's fonts (see typo & colors in ZIP file)
- Please use our company logo (see ZIP file).
- The design also needs to convey a strong sense of professionalism as we are an animal "healthcare" brand.
- If you want to include a dog picture, we would prefer you to use a picture of our official brand ambassador (see ZIP file).
- Only original work (no plagiarism will be accepted).

Please don't hesitate to send us a message if you have any questions about the brand, the product or the design requirements.

We look forward to seeing your designs & working on this together !

Thanks & regards,
Marcus

Target Market(s)

Dog owners

Font styles to use
Other font styles liked:
• See ZIP file

Requirements
Must have
• Brand fonts (see typo & colors in ZIP file)
Brand colors (see typo & colors in ZIP file)

```html
<!DOCTYPE html>
<html lang="en">
<head>
<meta charset="UTF-8">
<title>VERDABALM Soothing Balm – Jar Labels</title>
<link href="https://fonts.googleapis.com/css2?family=Montserrat:wght@400;500;600;700;800&display=swap" rel="stylesheet">
<style>
  :root {
    --bg: #f2f3f3;
    --label: #ffffff;
    --rim: #c9cccd;
    --rim-dark: #a9adaf;
    --teal: #3f9e8c;
    --teal-dark: #2f7f70;
    --grey: #5f6467;
    --grey-light: #8b9093;
    --photo-a: #a08c7c;
    --photo-b: #d9d2c9;
  }
  * { box-sizing: border-box; margin: 0; padding: 0; }
  html, body { width: 1200px; height: 2224px; overflow: hidden; }
  body {
    background: var(--bg);
    font-family: "Montserrat", sans-serif;
    color: var(--grey);
    position: relative;
  }
  .label {
    position: absolute;
    left: 210px;
    width: 780px;
    height: 780px;
    border-radius: 50%;
    background: var(--label);
    border: 26px solid var(--rim);
    box-shadow: inset 0 0 0 6px var(--rim-dark);
  }
  .label--front { top: 170px; }
  .label--back { top: 1250px; }

  /* front */
  .brand {
    position: absolute; top: 92px; left: 0; right: 0;
    text-align: center;
  }
  .brand__mark {
    display: block; width: 40px; height: 40px; margin: 0 auto 14px;
    border-radius: 50%; background: var(--teal);
  }
  .brand__name {
    font-size: 50px; font-weight: 600; letter-spacing: 4px; color: var(--grey);
  }
  .brand__tag {
    font-size: 15px; letter-spacing: 3px; color: var(--grey-light); margin-top: 2px;
  }
  .product {
    position: absolute; top: 268px; left: 0; right: 0; text-align: center;
  }
  .product__name {
    font-size: 40px; font-weight: 800; letter-spacing: 3px; color: var(--teal);
  }
  .product__type {
    font-size: 22px; font-weight: 500; letter-spacing: 3px; color: var(--grey); margin-top: 4px;
  }
  .benefits {
    position: absolute; top: 368px; left: 120px; right: 120px;
    background: var(--teal); color: #fff;
    text-align: center; font-size: 16px; font-weight: 600; letter-spacing: 3px;
    padding: 9px 0; border-radius: 4px;
  }
  .photo {
    position: absolute; top: 430px; left: 50%; transform: translateX(-50%);
    width: 210px; height: 210px; border-radius: 50%;
    background: radial-gradient(circle at 50% 45%, var(--photo-a), var(--photo-b) 75%);
  }
  .side {
    position: absolute; top: 50%; font-size: 17px; font-weight: 600;
    letter-spacing: 2px; color: var(--teal);
  }
  .side--left { left: 28px; transform: translateY(-50%) rotate(-90deg); }
  .side--right { right: 28px; transform: translateY(-50%) rotate(90deg); color: var(--grey-light); }

  /* back */
  .info {
    position: absolute; top: 96px; left: 110px; right: 110px;
    text-align: center; font-size: 15px; line-height: 1.5; color: var(--grey);
  }
  .info__heading {
    color: var(--teal); font-weight: 700; letter-spacing: 2px; font-size: 17px;
  }
  .info__block { margin-bottom: 22px; }
  .info__rule { width: 62%; height: 2px; background: var(--teal); margin: 0 auto 22px; }
  .info__small { font-size: 13px; color: var(--grey-light); }
</style>
</head>
<body>

<section class="label label--front">
  <div class="brand">
    <span class="brand__mark"></span>
    <div class="brand__name">VERDALIS</div>
    <div class="brand__tag">pet care</div>
  </div>
  <div class="product">
    <div class="product__name">VERDABALM</div>
    <div class="product__type">SOOTHING BALM</div>
  </div>
  <div class="benefits">REPAIR · NOURISH · PROTECT</div>
  <div class="photo" role="img" aria-label="Photo of the brand ambassador dog"></div>
  <div class="side side--left">CBD 100mg</div>
  <div class="side side--right">40g / 1.4oz</div>
</section>

<section class="label label--back">
  <div class="info">
    <div class="info__block">
      <div class="info__heading">SOOTHING RELAXATION</div>
      <p>This balm repairs, nourishes and protects your dog's sensitive paws. Its hemp extract helps calm and supports daily comfort and wellbeing.</p>
    </div>
    <div class="info__rule"></div>
    <div class="info__block">
      <div class="info__heading">RECOMMENDED USE</div>
      <p>Take a small amount and gently massage into clean, dry paws once or twice a day. For external use only.</p>
    </div>
    <div class="info__block info__small">
      <p><strong>INGREDIENTS:</strong> Shea Butter, Beeswax, Coconut Oil, Hemp Extract (CBD), Vitamin E.</p>
    </div>
    <div class="info__block info__small">
      <p>Distributed by: VERDALIS Care Ltd<br>12 Meadow Lane, Greenfield</p>
    </div>
  </div>
</section>

</body>
</html>
```